A clean crisp business card for a Landscape Construction company. Designed to be easy to read contact/ info and also be appealing/interesting, unlike a traditional business card.

Industry/Entity Type

Landscape Construction

Contact Information for Business Card

Company name : Brambleway Landscape Construction, phone number: (877) 61Vista, website:Bramblewaylandscapes.example, Email, sales@bramblewaylandscapes.example

Requirements
Nice to have
• Luxurious finishes/ details…. Icons or emblems next to contact info
Should not have
• Clipart or general pictures

```html
<!DOCTYPE html>
<html lang="en">
<head>
<meta charset="utf-8">
<title>Brambleway Landscape Construction – Business Card</title>
<link href="https://fonts.googleapis.com/css2?family=Cinzel:wght@600&family=Open+Sans:wght@400;600&display=swap" rel="stylesheet">
<style>
  :root {
    --backdrop: #d9d9d7;
    --card-white: #fbfbfb;
    --brand-blue: #1f62c2;
    --brand-green: #8cc63f;
    --gradient-blue: #1764c6;
    --gradient-teal: #3f9a9a;
    --gradient-green: #a6d44a;
    --ink: #2a2a2a;
    --reverse: #ffffff;
  }
  * { box-sizing: border-box; margin: 0; padding: 0; }
  html, body { width: 1200px; height: 675px; overflow: hidden; }
  body {
    background: var(--backdrop);
    font-family: "Open Sans", Arial, sans-serif;
    position: relative;
  }
  .card {
    position: absolute;
    top: 194px;
    width: 504px;
    height: 288px;
    border-radius: 18px;
    box-shadow: 0 10px 28px rgba(0,0,0,.18);
    overflow: hidden;
  }
  .card--front { left: 64px; background: var(--card-white); }
  .card--back {
    left: 632px;
    background: linear-gradient(135deg, var(--gradient-blue) 0%, var(--gradient-teal) 48%, var(--gradient-green) 100%);
    display: flex;
    align-items: center;
    justify-content: center;
  }

  .brand-name {
    position: absolute;
    left: 48px;
    top: 48px;
    color: var(--brand-blue);
    font-weight: 600;
    line-height: 1;
  }
  .brand-name__main { display: block; font-size: 40px; letter-spacing: .5px; }
  .brand-name__sub { display: block; font-size: 13.5px; letter-spacing: 3.6px; margin-top: 6px; text-transform: uppercase; }

  .rule-pair {
    position: absolute;
    left: 32px;
    top: 146px;
    width: 400px;
  }
  .rule-pair span { display: block; height: 2px; }
  .rule-pair .rule--green { background: var(--brand-green); margin-bottom: 3px; }
  .rule-pair .rule--blue { background: var(--brand-blue); }

  .contact-list {
    position: absolute;
    left: 36px;
    top: 176px;
    list-style: none;
  }
  .contact-list li {
    display: flex;
    align-items: center;
    gap: 10px;
    font-size: 14.5px;
    color: var(--ink);
    height: 27px;
  }
  .contact-icon { width: 17px; height: 17px; flex: none; }

  .person {
    position: absolute;
    right: 44px;
    top: 170px;
    width: 112px;
    text-align: right;
    border-bottom: 2px solid var(--brand-blue);
    padding-bottom: 3px;
  }
  .person__name {
    font-family: "Cinzel", Georgia, serif;
    font-size: 24px;
    color: var(--brand-blue);
    line-height: 1.1;
  }
  .person__role { font-size: 13px; color: var(--ink); line-height: 1.3; }

  .back-name {
    color: var(--reverse);
    font-weight: 600;
    text-align: center;
    line-height: 1;
  }
  .back-name__main { display: block; font-size: 44px; letter-spacing: .5px; }
  .back-name__sub { display: block; font-size: 14px; letter-spacing: 4px; margin-top: 8px; text-transform: uppercase; }
</style>
</head>
<body>
  <section class="card card--front" aria-label="Card front">
    <div class="brand-name">
      <span class="brand-name__main">Brambleway</span>
      <span class="brand-name__sub">Landscape Construction</span>
    </div>

    <div class="rule-pair"><span class="rule--green"></span><span class="rule--blue"></span></div>

    <ul class="contact-list">
      <li>
        <svg class="contact-icon" viewBox="0 0 20 20" aria-hidden="true">
          <circle cx="10" cy="10" r="10" fill="#8cc63f"/>
          <path d="M6.5 5.5 L8.3 5.3 L9 8 L8 9 Q9 11 11 12 L12 11 L14.7 11.7 L14.5 13.5 Q9 14.5 5.8 8.5 Z" fill="#fff"/>
        </svg>
        <span>(877) 61Vista</span>
      </li>
      <li>
        <svg class="contact-icon" viewBox="0 0 20 20" aria-hidden="true">
          <circle cx="10" cy="10" r="10" fill="#8cc63f"/>
          <circle cx="10" cy="10" r="5" fill="none" stroke="#fff" stroke-width="1.3"/>
          <ellipse cx="10" cy="10" rx="2.2" ry="5" fill="none" stroke="#fff" stroke-width="1.1"/>
          <line x1="5" y1="10" x2="15" y2="10" stroke="#fff" stroke-width="1.1"/>
        </svg>
        <span>www.bramblewaylandscapes.example</span>
      </li>
      <li>
        <svg class="contact-icon" viewBox="0 0 20 20" aria-hidden="true">
          <circle cx="10" cy="10" r="10" fill="#8cc63f"/>
          <rect x="5" y="6.5" width="10" height="7" fill="#fff"/>
          <path d="M5 6.8 L10 10.5 L15 6.8" fill="none" stroke="#8cc63f" stroke-width="1"/>
        </svg>
        <span>sales@bramblewaylandscapes.example</span>
      </li>
    </ul>

    <div class="person">
      <div class="person__name">Name</div>
      <div class="person__role">Owner</div>
    </div>
  </section>

  <section class="card card--back" aria-label="Card back">
    <div class="back-name">
      <span class="back-name__main">Brambleway</span>
      <span class="back-name__sub">Landscape Construction</span>
    </div>
  </section>
</body>
</html>
```